Web Design Project for Energy Efficiency Consultancy

We require a website designed and preferably coded. The website will have around 6-8 pages of basic content with a "contact us" webform.

We are primarily after someone to take our logo, colour scheme and the rough layouts that we have produced and to turn them into a professional looking website.

Please refer to the attached documents for example layouts that we have put together in photoshop, example content, our logo and colour scheme.

We will accept a PSD file but our preference is certainly to have it coded.
Updates

We have attached some documents to the brief that provide more detail.

We have had a question about how projects can be loaded into Venture Lattice. Follow this link for more info http://www.venturelattice.com.au/support/dw#install

Target Market(s)

Builders, real estate agents, government agencies

Industry/Entity Type

It Professional

Requirements
Must have
• We are after a clean and professional look.
Nice to have
• We are keen to have the site fully coded in venture lattice as we have another website that has been built on VL and so we are familiar with how to use it.

```html
<!DOCTYPE html>
<html lang="en">
<head>
<meta charset="utf-8">
<title>Verdant Watt – your energy efficiency experts</title>
<link rel="stylesheet" href="https://fonts.googleapis.com/css2?family=Arimo:wght@400;700&family=Open+Sans:wght@300;400;600&display=swap">
<style>
:root{
  --bar-dark:#444;
  --header-green:#cfe0aa;
  --band-green:#8fcc0b;
  --ink:#1e1e1e;
  --tag-green:#8cb93a;
  --mark-green:#a9c66c;
  --panel-grey:#717171;
  --footer-top:#2e3033;
  --footer-bottom:#050505;
  --accent-lime:#c9e34a;
  --testimonial:#7c3636;
  --signature:#e32626;
  --dot-red:#e42a0c;
  --badge-blue:#1a5d92;
}
*{box-sizing:border-box;margin:0;padding:0}
html,body{width:1200px;height:1000px;overflow:hidden;background:#fff}
body{position:relative;font-family:"Arimo",Arial,sans-serif;color:var(--ink)}
.abs{position:absolute}
.top-strip{left:0;top:0;width:1200px;height:8px;background:var(--bar-dark)}
.header{left:0;top:8px;width:1200px;height:129px;background:var(--header-green);border-bottom:1px solid #e8f0d4}
.brand{left:242px;top:37px;height:90px;display:flex;align-items:center;gap:12px}
.brand-dot{width:90px;height:90px;border-radius:50%;background:var(--mark-green)}
.brand-name{font:400 30px/34px "Arimo",sans-serif;color:var(--ink);width:110px}
.tagline{left:490px;top:97px;font:300 19px "Open Sans",sans-serif;color:var(--tag-green)}
.call-now{left:722px;top:68px;font:400 17px "Arimo",sans-serif;color:var(--ink)}
.search{left:770px;top:96px;width:166px;height:22px;background:#f2f2f2;border:1px solid #d5d5d5;font-size:8px;color:#999;padding:6px 7px}
.search-btn{right:0;top:0;width:20px;height:20px}
.green-band{left:0;top:137px;width:1200px;height:260px;background:var(--band-green)}
.grey-band{left:0;top:397px;width:1200px;height:365px;background:linear-gradient(#e4e4e4,#cfcfcf)}
.nav{left:242px;top:147px;width:678px;height:28px;background:linear-gradient(#3a3a3a,#000)}
.nav a{position:absolute;font:400 12.5px/28px "Open Sans",sans-serif;color:#fff;text-decoration:none;white-space:nowrap}
.slider{left:242px;top:176px;width:678px;height:285px;background:#eef1f3}
.slide{left:16px;top:7px;width:653px;height:249px;background:linear-gradient(#5d6062 0%,#9a9c9d 55%,#3f4142 62%,#2b2c2d 100%)}
.slide-caption{left:12px;bottom:13px;font:400 17px "Arimo",sans-serif;color:#fff}
.dot{top:264px;width:13px;height:13px;border-radius:50%;background:#444;border:2px solid #777}
.dot.active{background:var(--dot-red);border-color:#b01}
.slider-shadow{left:265px;top:461px;width:665px;height:6px;background:radial-gradient(ellipse at center,rgba(0,0,0,.35),rgba(0,0,0,0) 70%)}
.intro-title{left:253px;top:474px;font:400 25px "Arimo",sans-serif;color:#111}
.intro-text{left:255px;top:505px;width:450px;font:400 7.4px/14.8px "Arimo",sans-serif;color:#222}
.services-panel{left:254px;top:581px;width:457px;height:173px;background:var(--panel-grey);color:#fff;padding:3px 14px;font-size:7.4px;line-height:8.8px}
.services-panel h3{font:400 10.5px/14px "Arimo",sans-serif;margin:0 0 6px}
.services-panel .row{display:flex;margin-bottom:8px}
.services-panel .st{width:33px;flex:none}
.contact-head{left:720px;top:473px;width:196px;height:23px;background:linear-gradient(#3a3a3a,#000);color:var(--band-green);font:400 12px/23px "Open Sans",sans-serif;padding-left:12px}
.form-label{left:741px;font:400 9px "Open Sans",sans-serif;color:#222}
.field{left:783px;width:86px;height:17px;background:#f1f1f1;border:1px solid #ccc}
.submit{left:783px;top:641px;width:80px;height:19px;background:linear-gradient(#444,#111);color:#fff;font:700 7px/19px "Arimo",sans-serif;padding-left:19px;border-radius:2px}
.submit span{position:absolute;right:0;top:0;width:18px;height:19px;border-left:1px solid #666;text-align:center}
.testi-title{left:723px;top:671px;font:400 18px "Arimo",sans-serif;color:var(--testimonial)}
.testi-text{left:727px;top:698px;width:192px;font:400 7.6px/14px "Arimo",sans-serif;color:#222}
.testi-sign{left:848px;top:742px;font:400 10px "Arimo",sans-serif;color:var(--signature)}
.footer{left:0;top:762px;width:1200px;height:166px;background:linear-gradient(var(--footer-top),var(--footer-bottom))}
.promo{left:208px;top:778px;width:254px;height:126px;background:#3b3b3b;padding:4px 8px}
.promo h4{font:700 11px "Arimo",sans-serif;color:#fff;margin-bottom:3px}
.promo-art{width:230px;height:100px;background:linear-gradient(135deg,#e2953f,#c9a67a 50%,#eeeae2)}
.foot-line{font:700 8px "Arimo",sans-serif;color:var(--accent-lime);white-space:nowrap}
.divider{top:785px;width:1px;height:115px;background:#aaa}
.foot-h{top:788px;font:700 10.5px "Arimo",sans-serif;color:#fff}
.foot-list{left:639px;top:811px;list-style:none;font:700 8px/14px "Arimo",sans-serif;color:var(--accent-lime)}
.foot-address{left:819px;top:811px;font:700 8px/14px "Arimo",sans-serif;color:#fff}
.foot-address b{color:var(--accent-lime)}
.social{top:890px;width:11px;height:11px;border-radius:2px}
.bottom-rule{left:260px;top:931px;width:676px;height:1px;background:#ccc}
.bottom-logo{left:204px;top:941px;width:114px;height:52px;border-radius:8px;background:var(--header-green);display:flex;align-items:center;justify-content:center;gap:6px;font:400 12px "Arimo",sans-serif;color:var(--ink)}
.bottom-logo i{width:20px;height:20px;border-radius:50%;background:var(--mark-green)}
.copyright{left:327px;top:951px;font:400 7.5px "Arimo",sans-serif;color:#333}
.bottom-links{left:559px;top:951px;font:400 7.5px "Arimo",sans-serif;color:#333}
.bottom-call{left:339px;top:972px;font:400 13px "Arimo",sans-serif;color:#111}
.badge-a{left:649px;top:941px;width:124px;height:47px;background:var(--badge-blue);border-radius:3px}
.badge-b{left:783px;top:952px;width:142px;height:26px;background:#2a2a2a;border-radius:3px}
</style>
</head>
<body>
<div class="abs top-strip"></div>
<header class="abs header"></header>
<div class="abs brand"><span class="brand-dot"></span><span class="brand-name">Verdant Watt</span></div>
<div class="abs tagline">your energy efficiency experts!</div>
<div class="abs call-now">Call us Now! :&nbsp; 0255501234</div>
<div class="abs search">Search our site
  <svg class="abs search-btn" viewBox="0 0 20 20"><rect width="20" height="20" fill="#ddd"/><circle cx="9" cy="9" r="3.2" fill="none" stroke="#555" stroke-width="1.4"/><line x1="11.4" y1="11.4" x2="14.5" y2="14.5" stroke="#555" stroke-width="1.6"/></svg>
</div>

<div class="abs green-band"></div>
<div class="abs grey-band"></div>

<nav class="abs nav">
  <a style="left:14px">Home</a><a style="left:62px">About us</a><a style="left:128px">Verdant Watt</a><a style="left:219px">Residential</a><a style="left:300px">Commercial</a><a style="left:385px">Contact us</a>
</nav>

<section class="abs slider">
  <div class="abs slide" role="img" aria-label="Infrared thermal visualisation of a single family house">
    <div class="abs slide-caption">THERMAL PERFORMANCE ASSESSMENT</div>
  </div>
  <div class="abs dot active" style="left:592px"></div>
  <div class="abs dot" style="left:612px"></div>
  <div class="abs dot" style="left:633px"></div>
  <div class="abs dot" style="left:654px"></div>
</section>
<div class="abs slider-shadow"></div>

<h1 class="abs intro-title">Introduction</h1>
<p class="abs intro-text">Lorem Ipsum is simply dummy text of the printing and typesetting industry. Lorem Ipsum has been the industry's standard dummy<br>text ever since the 1500s, when an unknown printer took a galley of type and scrambled it to make a type specimen book. It has<br>survived not only five centuries, but also the leap into electronic typesetting, remaining essentially unchanged. It was popularised in the<br>1960s with the release of Letraset sheets containing Lorem Ipsum passages, and more recently with desktop publishing software like<br>Aldus PageMaker including versions of Lorem Ipsum.</p>

<section class="abs services-panel">
  <h3>RESIDENTIAL BUILDINGS</h3>
  <div class="row"><span class="st">ACT &nbsp; -</span><span>BCA Compliance for NEW Single Dwellings or Unit Developments<br>BCA Compliance for Alterations and Extensions.<br>Property sale (Mandatory Disclosure)</span></div>
  <div class="row"><span class="st">NSW &nbsp; -</span><span>BCA and BASIX Compliance for new Single Dwellings or Unit Developments<br>BCA and BASIX Compliance for Alterations and Extensions</span></div>
  <h3>COMMERCIAL BUILDINGS</h3>
  <div class="row"><span class="st">ACT &nbsp; -</span><span>Building Classes 3 to 9 - &nbsp;BAC Section J Compliance &nbsp;- &nbsp;Deemed to Satisfy<br>&nbsp; &nbsp; &nbsp; &nbsp; &nbsp; &nbsp; &nbsp;and Verification Method<br>Building Class 2 - ACTHERS Thermal Assessment</span></div>
  <div class="row"><span class="st">NSW &nbsp; -</span><span>Building Classes 3 to 9 - &nbsp;BAC Section J Compliance &nbsp;- &nbsp;Deemed to Satisfy<br>&nbsp; &nbsp; &nbsp; &nbsp; &nbsp; &nbsp; &nbsp;and Verification Method<br>Building Class 2 - ACTHERS Thermal Assessment</span></div>
</section>

<div class="abs contact-head">Contact Info</div>
<div class="abs form-label" style="top:507px">Name</div><div class="abs field" style="top:504px"></div>
<div class="abs form-label" style="top:532px">E-mail</div><div class="abs field" style="top:529px"></div>
<div class="abs form-label" style="top:558px">Phone</div><div class="abs field" style="top:555px"></div>
<div class="abs form-label" style="top:583px">Message</div><div class="abs field" style="top:580px;height:49px"></div>
<div class="abs submit">SUBMIT<span>&#9656;</span></div>

<h2 class="abs testi-title">Testimonials</h2>
<p class="abs testi-text">Lorem Ipsum is simply dummy text of the printing and<br>typesetting industry. Lorem Ipsum has been the<br>industry's standard dummy text ever since the 1500s,</p>
<div class="abs testi-sign">..John Doe</div>

<footer class="abs footer"></footer>
<div class="abs promo">
  <h4>THERMAL PERFORMANCE ASSESSMENTS</h4>
  <div class="promo-art" role="img" aria-label="Promotional panel with interior room photo and house energy diagram"></div>
</div>
<div class="abs foot-line" style="left:484px;top:798px">Phone: 0255501234</div>
<div class="abs foot-line" style="left:484px;top:812px">Tom: 0400 555 118</div>
<div class="abs foot-line" style="left:484px;top:826px">Laura: 0400 555 247</div>
<div class="abs foot-line" style="left:480px;top:849px">E-mail:</div>
<div class="abs foot-line" style="left:480px;top:858px">tom.reid@verdantwatt.com.au</div>
<div class="abs foot-line" style="left:480px;top:879px">laura.finch@verdantwatt.com.au</div>
<div class="abs divider" style="left:631px"></div>
<div class="abs divider" style="left:786px"></div>
<div class="abs foot-h" style="left:638px">Our Services</div>
<ul class="abs foot-list"><li>Home</li><li>About us</li><li>Verdant Watt</li><li>Residential</li><li>Commercial</li><li>Contact us</li></ul>
<div class="abs foot-h" style="left:818px">Contact</div>
<div class="abs foot-address"><b>VERDANT WATT</b><br>PO BOX XX<br>Harrowfield<br>ACT 2999</div>
<div class="abs social" style="left:820px;background:#4aa6d6"></div>
<div class="abs social" style="left:835px;background:#3b5998"></div>
<div class="abs social" style="left:850px;background:#f28a1c"></div>

<div class="abs bottom-rule"></div>
<div class="abs bottom-logo"><i></i>Verdant Watt</div>
<div class="abs copyright">© Copyright VERDANTWATT.COM.AU &nbsp;All Rights Reserved</div>
<div class="abs bottom-links">Home | Contact | RSS</div>
<div class="abs bottom-call">Call us Now! :&nbsp; 0255501234</div>
<div class="abs badge-a"></div>
<div class="abs badge-b"></div>
</body>
</html>
```